Company truck branding

I'm looking for a clean wrap design for my company vehicles and trailers. It needs to fit our branding based on logo. Most of our trucks and trailers are grey but we do have white trucks also. You can visit our website Verodalandscaping.com or our instagram at verodalandscaping

Industry/Entity Type

Landscaping

Font styles to use
Serif
Sans Serif

Colors

Designer to choose only greyscale colors for use in the design.

Requirements
Must have
• Want a Clean MODERN DESIGN
Should not have
• Don’t want grass or anything that is not on my logo.

```html
<!DOCTYPE html>
<html lang="en">
<head>
<meta charset="utf-8">
<title>Veroda Landscaping – Vehicle Wrap</title>
<link rel="stylesheet" href="https://fonts.googleapis.com/css2?family=Cinzel:wght@400;600&family=Montserrat:wght@400&display=swap">
<style>
  :root{
    --ink:#1f1d1c;
    --paper:#ffffff;
    --wrap-white:#f4f4f3;
    --tree-grey:#6a6968;
    --accent:#a88b68;
    --canvas:#ffffff;
  }
  *{margin:0;padding:0;box-sizing:border-box}
  html,body{width:1200px;height:1200px;overflow:hidden;background:var(--canvas)}
  body{position:relative;font-family:"Cinzel",serif}

  .wrap-panel{position:absolute;left:12px;width:1176px;overflow:hidden}
  .wrap-panel svg{position:absolute;inset:0;display:block}

  /* truck door layout */
  .truck-wrap{top:51px;height:426px;background:var(--wrap-white)}
  .truck-name{position:absolute;left:654px;top:188px;width:270px;text-align:center;color:var(--ink);font-family:"Cinzel",serif;font-weight:600;line-height:1}
  .truck-name .name-main{display:block;font-size:37px;letter-spacing:1px}
  .truck-name .name-sub{display:block;font-size:11px;letter-spacing:5px;margin-top:6px}
  .truck-phone{position:absolute;left:898px;top:180px;width:200px;text-align:center;color:var(--paper);font-family:"Cinzel",serif;font-size:19px}
  .truck-web{position:absolute;left:654px;top:292px;width:270px;text-align:center;color:var(--ink);font-family:"Cinzel",serif;font-size:10px;letter-spacing:.3px}

  /* trailer layout */
  .trailer-wrap{top:520px;height:470px;background:var(--ink)}
  .trailer-band{position:absolute;left:0;right:0;top:138px;height:185px;background:var(--wrap-white)}
  .trailer-trees{position:absolute;left:0;right:0;bottom:0;height:140px;background:linear-gradient(to top,rgba(106,105,104,.75),rgba(106,105,104,0))}
  .trailer-name{position:absolute;left:120px;top:162px;width:460px;text-align:center;color:var(--ink);font-family:"Cinzel",serif;font-weight:600;line-height:1}
  .trailer-name .name-main{display:block;font-size:88px;letter-spacing:2px}
  .trailer-name .name-sub{display:block;font-size:30px;letter-spacing:14px;margin-top:10px}
  .trailer-phone{position:absolute;left:430px;top:52px;width:460px;text-align:center;color:var(--paper);font-family:"Cinzel",serif;font-size:46px}
  .service-list{position:absolute;left:578px;top:198px;list-style:none;color:var(--ink);font-family:"Cinzel",serif;font-size:17px;line-height:19px}
  .service-list li{position:relative;padding-left:16px}
  .service-list li::before{content:"";position:absolute;left:0;top:6px;width:8px;height:8px;border-radius:50%;background:var(--accent)}
  .trailer-web{position:absolute;left:430px;top:346px;width:460px;text-align:center;color:var(--paper);font-family:"Cinzel",serif;font-size:21px}
</style>
</head>
<body>

<section class="wrap-panel truck-wrap" aria-label="Truck door wrap">
  <svg viewBox="0 0 1176 426" width="1176" height="426" aria-hidden="true">
    <defs>
      <linearGradient id="tree-fade" x1="0" y1="1" x2="0" y2="0">
        <stop offset="0" stop-color="#6a6968" stop-opacity=".8"/>
        <stop offset="1" stop-color="#6a6968" stop-opacity="0"/>
      </linearGradient>
    </defs>
    <polygon points="0,426 0,160 330,160 720,426" fill="#1f1d1c"/>
    <polygon points="640,0 1176,0 1176,230 980,230" fill="#1f1d1c"/>
    <polygon points="0,426 0,250 460,250 720,426" fill="url(#tree-fade)" role="img" aria-label="Silhouette of evergreen trees"/>
  </svg>
  <div class="truck-name"><span class="name-main">VERODA</span><span class="name-sub">LANDSCAPING</span></div>
  <div class="truck-phone">123-456-7890</div>
  <div class="truck-web">VERODALANDSCAPING.COM</div>
</section>

<section class="wrap-panel trailer-wrap" aria-label="Trailer side wrap">
  <div class="trailer-band"></div>
  <div class="trailer-trees" role="img" aria-label="Row of evergreen tree silhouettes"></div>
  <div class="trailer-phone">123-456-7890</div>
  <div class="trailer-name"><span class="name-main">VERODA</span><span class="name-sub">LANDSCAPING</span></div>
  <ul class="service-list">
    <li>PLANT HEALTHCARE</li>
    <li>LANSDCAPE MAINTENANCE</li>
    <li>HARDSCAPES</li>
    <li>DESIGN BUILD</li>
  </ul>
  <div class="trailer-web">VERODALANDSCAPING.COM</div>
</section>

</body>
</html>
```